High-end construction company needs a business card design

We need a modern looking business card that draws people in, is memorable and looks so good people will want to sick it on their fridges.
On the first side what is needed are:
Logo
My name - Tomas Brevik
Title - Managing Director
Website - www.kelvora.co.uk
Email - tomas@kelvora.co.uk
Telephone - 020 4917 2365
Mobile - 07845139072
On the back side was is needed is a list of all the services we provide:
-Kitchen Renovations
-Bathroom Renovations
-House Renovations
-Garage Conversions
-Extensions
-Loft Conversions
-Conservatories
-Carpentry
-Tiling
-Electrical
-Plumbing & Heating
-Bricklaying
-Landscaping
-Decorating
-Plastering
We would like the colours to be the same shades as on the logo with grey or black for the words.
Target Market(s)
Anyone who needs building work done
Contact Information for Business Card
This business card is for a construction company which strives to deliver excellent service and quality.
The look and feel of the card should represent this.
Requirements
Must have
- On the first side what is needed are:
Logo
My name - Tomas Brevik
Title - Managing Director
Website - www.kelvora.co.uk
Email - tomas@kelvora.co.uk
Telephone - 020 4917 2365
Mobile - 07845139072
Nice to have
- Cool looking features

```html
<!DOCTYPE html>
<html lang="en">
<head>
<meta charset="utf-8">
<title>Kelvora Construction Ltd – Business Card</title>
<link href="https://fonts.googleapis.com/css2?family=Montserrat:wght@300;400;600;700&display=swap" rel="stylesheet">
<style>
  :root{
    --page-bg:#e4e4e4;
    --card-white:#ffffff;
    --brand-green:#5cad45;
    --brand-green-dark:#3f8f35;
    --back-green-light:#66a35e;
    --back-green-dark:#2f7a2f;
    --text-grey:#555a5e;
    --rule-grey:#8a8a8a;
    --white:#ffffff;
  }
  *{box-sizing:border-box;margin:0;padding:0}
  html,body{width:1200px;height:1200px;overflow:hidden}
  body{background:var(--page-bg);font-family:"Montserrat",sans-serif;position:relative}

  .card{position:absolute;left:262px;width:686px;height:392px;box-shadow:0 18px 30px rgba(0,0,0,.18)}
  .card--front{top:165px;background:var(--card-white)}
  .card--back{top:653px;background:linear-gradient(30deg,var(--back-green-dark) 0%,var(--back-green-light) 100%);color:var(--white)}

  /* front */
  .brand{position:absolute;left:106px;top:150px;width:214px;text-align:center;color:var(--brand-green);font-weight:700}
  .brand__name{font-size:44px;line-height:1;letter-spacing:1px}
  .brand__sub{font-size:13.5px;letter-spacing:2px;margin-top:8px}
  .divider{position:absolute;left:349px;top:128px;width:1px;height:138px;background:var(--rule-grey)}
  .person{position:absolute;left:380px;top:122px}
  .person__name{font-size:24px;font-weight:700;color:var(--brand-green);letter-spacing:.6px;line-height:1.1}
  .person__title{font-size:14px;font-weight:600;color:var(--brand-green-dark);margin-top:2px}
  .contacts{list-style:none;margin-top:14px}
  .contacts li{display:flex;align-items:center;height:20.7px;font-size:16px;font-weight:400;color:var(--text-grey);letter-spacing:.3px}
  .contacts svg{width:12px;height:12px;margin-right:10px;fill:var(--brand-green-dark);flex:none}

  /* back */
  .back-brand{position:absolute;left:149px;top:120px;width:370px;text-align:center;font-weight:700;font-size:58px;letter-spacing:4px;line-height:1}
  .ground-line{position:absolute;left:149px;top:208px;width:370px;height:2px;background:var(--white)}
  .services{position:absolute;left:0;top:232px;width:100%;text-align:center;font-size:15.5px;font-weight:300;line-height:21.5px;letter-spacing:.2px}
  .check{display:inline-block;width:12px;height:12px;border:1.3px solid var(--white);margin:0 3px;position:relative;vertical-align:-1px}
  .check::after{content:"";position:absolute;left:3px;top:0;width:3px;height:6px;border:solid var(--white);border-width:0 1.6px 1.6px 0;transform:rotate(40deg)}
  .social{position:absolute;top:335px;left:50%;transform:translateX(-50%);display:flex;gap:4px}
  .social__item{width:22px;height:22px;border:1.6px solid var(--white);border-radius:6px}
</style>
</head>
<body>

<section class="card card--front" aria-label="Business card front">
  <div class="brand">
    <div class="brand__name">KELVORA</div>
    <div class="brand__sub">CONSTRUCTION LTD</div>
  </div>
  <div class="divider"></div>
  <div class="person">
    <h1 class="person__name">TOMAS BREVIK</h1>
    <p class="person__title">Managing Director</p>
    <ul class="contacts">
      <li><svg viewBox="0 0 24 24"><path d="M6.6 10.8c1.4 2.8 3.8 5.1 6.6 6.6l2.2-2.2c.3-.3.7-.4 1-.2 1.1.4 2.3.6 3.6.6.6 0 1 .4 1 1V20c0 .6-.4 1-1 1C10.6 21 3 13.4 3 4c0-.6.4-1 1-1h3.5c.6 0 1 .4 1 1 0 1.3.2 2.5.6 3.6.1.3 0 .7-.2 1z"/></svg>020 4917 2365</li>
      <li><svg viewBox="0 0 24 24"><path d="M7 1h10a2 2 0 0 1 2 2v18a2 2 0 0 1-2 2H7a2 2 0 0 1-2-2V3a2 2 0 0 1 2-2zm0 3v14h10V4z"/></svg>07845139072</li>
      <li><svg viewBox="0 0 24 24"><path d="M2 5h20v14H2zm2 2v.5l8 5 8-5V7l-8 5z"/></svg>tomas@kelvora.co.uk</li>
      <li><svg viewBox="0 0 24 24"><path d="M12 2a10 10 0 1 0 0 20 10 10 0 0 0 0-20zm-1 17.9A8 8 0 0 1 4.2 10.6L9 15.4v1a2 2 0 0 0 2 2zm6.9-2.5A2 2 0 0 0 16 16h-1v-3a1 1 0 0 0-1-1H8v-2h2a1 1 0 0 0 1-1V7h2a2 2 0 0 0 2-2v-.4a8 8 0 0 1 2.9 12.8z"/></svg>www.kelvora.co.uk</li>
    </ul>
  </div>
</section>

<section class="card card--back" aria-label="Business card back">
  <div class="back-brand">KELVORA</div>
  <div class="ground-line"></div>
  <p class="services">
    Kitchen Renovations<span class="check"></span>Bathroom Renovations<span class="check"></span>House Renovations<br>
    Garage Conversions<span class="check"></span>Extensions<span class="check"></span>Loft Conversions<span class="check"></span>Conservatories<br>
    Carpentry<span class="check"></span>Tiling<span class="check"></span>Electrical<span class="check"></span>Plumbing &amp; Heating<span class="check"></span>Bricklaying<br>
    Landscaping<span class="check"></span>Decorating<span class="check"></span>Plastering
  </p>
  <div class="social" role="img" aria-label="Social media links">
    <span class="social__item"></span>
    <span class="social__item"></span>
    <span class="social__item"></span>
  </div>
</section>

</body>
</html>
```